Website design for Cambridge based systematic hedge fund

We have run previous craftmosaic competitions to design our company logo, business cards and the styling of our presentation deck (see attached files).
As the final step we are looking to get a website designed that is thematically consistent with these existing elements of our branding.
You can find some of our competitors websites below:
https://www.quelmarsh.example/
https://www.fenloor.example/
https://www.pyvart.example/
https://www.dulvet.example/
https://www.orbelmfunds.example/
https://www.valtrigo.example/
https://www.meskilfunds.example/home
We would like to have a website that works well on both mobile devices and desktops. Either just as one page that can be scrolled down, with links at the top that skips to certain sections, or a few separate pages that can be navigated by a top menu.
It should look professional, we are not after lots of animations or unnecessary transitions, and in particular the website must be smooth to navigate. We would like to avoid having peoples of people, we are happy to make use of elements from the presentation (for example the style of the cover slide, or the section slides with the faded bridge in the background), or 'financial' style images.
We would like to have the following sections for now. For some of these some example text has been provided, final text may change but it will be of similar length. For the other sections we are happy to just have template text for now. At the moment we are mainly interested to see styles/layouts as words can be added easily afterwards:
1) We will need a disclaimer pop up the first time someone visits the site (see for example the meskilfunds example).
2) Top page - company name, then in larger text "Bringing AI and Statistical Inference to Financial Markets", and somewhere in smaller text "Harlow Vectors is a quantitative asset manager with the singular focus of delivering algorithmic strategies that work"
3) "About us" section: will describe us as a company, details our approach, company values, and explains the company logo.
Example text:
"We deliver consistent alpha across liquid markets through the application of proprietary IP in Bayesian inference, machine learning and artificial intelligence. We are a multi-disciplinary team founded by experienced finance professionals from premier institutions, leading academics from the Thornbury Stellar Unit at Ashmere College and world-class software engineers.
Our logo portrays a sillhoute of the lattice walkway at Ashmere College. Our unique scientific approach allows us to bridge cutting-edge mathematical research and computing expertise with financial knowledge to bring algorithmns that work to liquid markets"
4) Hiring section, detailing our culture, what we are looking for.
Example text:
"We are always looking for exceptional talent to join our entrepreneurial team. We are looking for individuals who are creative thinkers, can demonstrate analytical rigour and are passionate about the intersection of science, finance and technology.
We prioritise having a company culture that promotes sharing ideas in a safe, collaborative research environment. We make sure that every member of the team has the oppertunity to explore their own ideas through weekly 'innovation time', and ensure that everyone gets the support they need to continue to grow as individuals within the company."
5) A section for news/press releases
6) Contact us area at the bottom with office location and email. We will need to list 3 addresses for our Cambridge, London and Singapore offices, along with a couple of contact emails or phone numbers
7) A client login button at the top that will take them to a different website (unrelated to this one).

```html
<!DOCTYPE html>
<html lang="en">
<head>
<meta charset="utf-8">
<title>Harlow Vectors</title>
<link rel="stylesheet" href="https://fonts.googleapis.com/css2?family=Oswald:wght@400;500&family=Poppins:wght@400;500;600&display=swap">
<style>
:root{
  --navy:#0a3470;
  --navy-deep:#072a5c;
  --footer:#082b5e;
  --blue:#1b5fae;
  --sky:#4f8fd6;
  --link:#2f6fc0;
  --ink:#1d3f6e;
  --text:#6a7380;
  --panel:#f2f3f5;
  --white:#ffffff;
}
*{margin:0;padding:0;box-sizing:border-box}
html,body{width:1200px;height:3800px;overflow:hidden;background:var(--white)}
body{font-family:"Poppins",sans-serif;color:var(--text);position:relative}
.heading{font-family:"Oswald",sans-serif;font-weight:400;text-transform:uppercase;color:var(--ink)}
.more{font-size:17px;font-weight:600;color:var(--ink);text-decoration:none;display:inline-flex;align-items:center;gap:14px}
.more::after{content:"→";font-weight:400;color:var(--link)}

/* hero */
.hero{position:absolute;left:0;top:0;width:1200px;height:720px;
  background:radial-gradient(ellipse at 60% 40%,#1653a0 0%,var(--navy) 55%,var(--navy-deep) 100%)}
.hero-pattern{position:absolute;inset:0}
.brand{position:absolute;left:80px;top:38px;font-family:"Oswald",sans-serif;font-weight:500;
  color:var(--white);font-size:30px;letter-spacing:2px;text-transform:uppercase}
.nav{position:absolute;right:90px;top:36px;display:flex;align-items:center;gap:34px}
.nav a{color:var(--white);font-size:15px;text-decoration:none;opacity:.92}
.nav a.active{opacity:.6}
.nav .login{border:2px solid var(--white);border-radius:20px;padding:4px 22px;opacity:1}
.hero-title{position:absolute;left:0;top:262px;width:1200px;text-align:center;
  font-family:"Oswald",sans-serif;font-weight:400;font-size:50px;line-height:62px;color:var(--white);text-transform:uppercase}
.hero-sub{position:absolute;left:0;top:388px;width:1200px;text-align:center;color:var(--white);font-size:17px;line-height:27px}

/* about */
.about-title{position:absolute;left:88px;top:898px;font-size:64px}
.rule{position:absolute;height:3px;background:var(--blue)}
.about-text{position:absolute;left:472px;top:832px;width:672px;font-size:17px;line-height:30px}
.about-more{position:absolute;left:472px;top:1040px}

/* hiring */
.hiring-panel{position:absolute;left:0;top:1232px;width:632px;height:648px;background:var(--panel)}
.hiring-photo{position:absolute;left:632px;top:1160px;width:568px;height:720px;
  background:linear-gradient(160deg,#9aa3ab 0%,#5d6670 45%,#2f3a47 100%)}
.hiring-title{position:absolute;left:88px;top:1418px;font-size:64px}
.hiring-text{position:absolute;left:88px;top:1512px;width:470px;font-size:16px;line-height:29px}
.hiring-more{position:absolute;left:88px;top:1688px}

/* news */
.news-title{position:absolute;left:88px;top:2004px;font-size:64px}
.news-img{position:absolute}
.news-one-img{left:100px;top:2152px;width:388px;height:256px;background:linear-gradient(135deg,#f4f4f2,#c9ccd0)}
.news-two-img{left:532px;top:2460px;width:580px;height:388px;background:linear-gradient(135deg,#8f8a7d,#d6d4cc 60%,#6f6a60)}
.news-three-img{left:88px;top:2920px;width:376px;height:252px;background:linear-gradient(135deg,#b99a72,#d9d2c6 55%,#6b5a47)}
.news-band{position:absolute;left:0;top:2520px;width:660px;height:460px;
  background:linear-gradient(135deg,#5c9ae0,var(--sky) 60%,#3f80cc)}
.news-item{position:absolute;width:470px}
.news-item h3{font-family:"Oswald",sans-serif;font-weight:400;font-size:26px;text-transform:uppercase;color:var(--ink);margin-bottom:10px}
.news-item p{font-size:16px;line-height:26px}
.news-item .read{display:block;margin-top:6px;font-size:17px;font-weight:600;color:var(--link);text-decoration:none}
.news-item.on-blue h3,.news-item.on-blue p,.news-item.on-blue .read{color:var(--white)}

/* footer */
.footer{position:absolute;left:0;top:3288px;width:1200px;height:512px;background:var(--footer)}
.footer-map{position:absolute;left:500px;top:40px;width:640px;height:340px;
  background:radial-gradient(ellipse,rgba(255,255,255,.07),rgba(255,255,255,0) 70%)}
.footer-brand{position:absolute;left:120px;top:186px;font-family:"Oswald",sans-serif;font-weight:500;
  color:var(--white);font-size:34px;letter-spacing:2px;text-transform:uppercase}
.office{position:absolute;color:var(--white);display:flex;gap:14px}
.office svg{flex:none;margin-top:2px}
.office h4{font-size:15px;font-weight:600;text-transform:uppercase;letter-spacing:.5px}
.office p{font-size:14px;opacity:.8;line-height:20px}
.footer-rule{position:absolute;left:80px;top:440px;width:1040px;height:1px;background:rgba(255,255,255,.2)}
.copyright{position:absolute;left:80px;top:470px;color:var(--white);font-size:14px;opacity:.85}
.social{position:absolute;left:940px;top:466px;display:flex;gap:26px}
.social span{width:18px;height:18px;border-radius:50%;background:rgba(255,255,255,.85);display:block}
.to-top{position:absolute;left:1124px;top:3736px;width:44px;height:44px;border-radius:50%;background:var(--link);
  display:flex;align-items:center;justify-content:center}
</style>
</head>
<body>

<header class="hero">
  <div class="hero-pattern" role="img" aria-label="Faint network of connected points over a deep blue background"></div>
  <div class="brand">Harlow Vectors</div>
  <nav class="nav">
    <a class="active">Home</a><a>About</a><a>Solutions</a><a>Careers</a><a>News</a><a>Contact</a><a class="login">Login</a>
  </nav>
  <h1 class="hero-title">Bringing AI and Statistical Inference<br>to Financial Markets</h1>
  <p class="hero-sub">Harlow Vectors is a quantitative asset manager with the singular<br>focus of delivering algorithmic strategies that work.</p>
</header>

<section>
  <h2 class="heading about-title">About Us</h2>
  <div class="rule" style="left:88px;top:978px;width:220px"></div>
  <p class="about-text">We deliver consistent alpha across liquid markets through the application of proprietary IP in Bayesian inference, machine learning and artificial intelligence. We are a multi-disciplinary team founded by experienced finance professionals from premier institutions, leading academics from the Thornbury Stellar Unit at Ashmere College and world-class software engineers.</p>
  <a class="more about-more">More</a>
</section>

<section>
  <div class="hiring-panel"></div>
  <div class="hiring-photo" role="img" aria-label="Professional holding a tablet in a modern office"></div>
  <h2 class="heading hiring-title">We Are Hiring</h2>
  <p class="hiring-text">We are always looking for exceptional talent to join our entrepreneurial team. We are looking for individuals who are creative thinkers, can demonstrate analytical rigour and are passionate about the intersection of science, finance and technology.</p>
  <a class="more hiring-more">More</a>
</section>

<section>
  <h2 class="heading news-title">Latest News</h2>
  <div class="rule" style="left:88px;top:2086px;width:260px"></div>

  <div class="news-img news-one-img" role="img" aria-label="Desk with a computer monitor in a bright office"></div>
  <article class="news-item" style="left:568px;top:2192px">
    <h3>News Heading Here</h3>
    <p>Lorem Ipsum is simply dummy text of the printing and typesetting industry. Lorem Ipsum has been the industry's standard dummy text ever since the 1500s, ...</p>
    <a class="read">Read More</a>
  </article>

  <div class="news-band" role="img" aria-label="Light blue band with faint connected network lines"></div>
  <div class="news-img news-two-img" role="img" aria-label="Team working with laptops around a table, seen from above"></div>
  <article class="news-item on-blue" style="left:88px;top:2672px">
    <h3>News Heading Here</h3>
    <p>Lorem Ipsum is simply dummy text of the printing and typesetting industry. Lorem Ipsum has been the industry's standard dummy text ever since the 1500s, ...</p>
    <a class="read">Read More</a>
  </article>

  <div class="news-img news-three-img" role="img" aria-label="Colleagues working together at a laptop"></div>
  <article class="news-item" style="left:732px;top:2956px">
    <h3>News Heading Here</h3>
    <p>Lorem Ipsum is simply dummy text of the printing and typesetting industry. Lorem Ipsum has been the industry's ...</p>
    <a class="read">Read More</a>
  </article>
</section>

<footer class="footer">
  <div class="footer-map" role="img" aria-label="Faint dotted world map"></div>
  <div class="footer-brand">Harlow Vectors</div>

  <div class="office" style="left:532px;top:166px">
    <svg width="16" height="20" viewBox="0 0 16 20"><path d="M8 0a7 7 0 0 0-7 7c0 5 7 13 7 13s7-8 7-13a7 7 0 0 0-7-7zm0 10a3 3 0 1 1 0-6 3 3 0 0 1 0 6z" fill="#fff"/></svg>
    <div><h4>Cambridge</h4><p>Some goes address here</p></div>
  </div>
  <div class="office" style="left:532px;top:240px">
    <svg width="16" height="20" viewBox="0 0 16 20"><path d="M8 0a7 7 0 0 0-7 7c0 5 7 13 7 13s7-8 7-13a7 7 0 0 0-7-7zm0 10a3 3 0 1 1 0-6 3 3 0 0 1 0 6z" fill="#fff"/></svg>
    <div><h4>London</h4><p>Some goes address here</p></div>
  </div>
  <div class="office" style="left:532px;top:314px">
    <svg width="16" height="20" viewBox="0 0 16 20"><path d="M8 0a7 7 0 0 0-7 7c0 5 7 13 7 13s7-8 7-13a7 7 0 0 0-7-7zm0 10a3 3 0 1 1 0-6 3 3 0 0 1 0 6z" fill="#fff"/></svg>
    <div><h4>Singapore</h4><p>Some goes address here</p></div>
  </div>
  <div class="office" style="left:872px;top:166px">
    <svg width="18" height="18" viewBox="0 0 18 18"><path d="M4 1l3 4-2 2c1 2 3 4 5 5l2-2 4 3-2 4C7 17 1 11 1 4z" fill="#fff"/></svg>
    <div><h4>Phone</h4><p>123 45677 5554</p></div>
  </div>
  <div class="office" style="left:872px;top:226px">
    <svg width="18" height="14" viewBox="0 0 18 14"><rect x="0" y="0" width="18" height="14" rx="2" fill="#fff"/><path d="M1 1l8 7 8-7" stroke="#082b5e" stroke-width="1.6" fill="none"/></svg>
    <div><h4>Email</h4><p>info@harlowvectors.example</p></div>
  </div>

  <div class="footer-rule"></div>
  <p class="copyright">©Copyright 2020 | All Rights Reserved</p>
  <div class="social"><span></span><span></span><span></span><span></span></div>
</footer>

<a class="to-top" aria-label="Back to top">
  <svg width="16" height="10" viewBox="0 0 16 10"><path d="M1 9l7-7 7 7" stroke="#fff" stroke-width="2" fill="none"/></svg>
</a>

</body>
</html>
```